Business card design for new brand

We have recently rebranded and need a new business card template.

We are an insurance underwriting agency. All of our products are sold via other partner companies, so these are just to pass on our details to other organisations.

We would like to see designs that use the colour green (current stationary generally uses lime green (rgb 142,190,63) and forest green (0,154,79) to comply with our logo's colours. We are happy with other shades of green.

Business cards need to include our logo, as well as space for:
1. Full name
2. Qualifications (optional)
3. Title
4. Office number
5. Mobile number
6. Email address

Our logo is enclosed here.

```html
<!DOCTYPE html>
<html lang="en">
<head>
<meta charset="utf-8">
<title>Verdant Cover – Business Card</title>
<link href="https://fonts.googleapis.com/css2?family=Poppins:wght@400;500;600;700&display=swap" rel="stylesheet">
<style>
  :root {
    --backdrop: #1b1b1b;
    --card: #161616;
    --white: #ffffff;
    --forest: #0f9a50;
    --forest-dark: #0d6a38;
    --lime: #8ebe3f;
    --text-soft: #e6e6e6;
  }
  * { box-sizing: border-box; margin: 0; padding: 0; }
  html, body {
    width: 1200px; height: 900px; overflow: hidden;
    background: var(--backdrop);
    font-family: "Poppins", sans-serif;
  }
  .sheet {
    width: 1200px; height: 900px;
    display: flex; flex-direction: column; align-items: center; justify-content: center;
    gap: 48px;
  }
  .card {
    position: relative;
    width: 660px; height: 377px;
    background: var(--card);
    box-shadow: 0 18px 40px rgba(0,0,0,.55);
    overflow: hidden;
  }
  /* Front */
  .card-front .person { position: absolute; left: 56px; top: 52px; }
  .person-name {
    color: var(--white); font-weight: 700; font-size: 28px; letter-spacing: .5px; line-height: 1.1;
  }
  .person-title {
    color: var(--forest); font-weight: 500; font-size: 19px; margin-top: 4px;
  }
  .contact-list { position: absolute; left: 56px; bottom: 52px; list-style: none; }
  .contact-item {
    display: flex; align-items: center; gap: 12px;
    color: var(--text-soft); font-size: 16px; line-height: 28px;
  }
  .contact-item svg { width: 16px; height: 16px; flex: none; }
  .brand-block {
    position: absolute; right: 60px; top: 50%; transform: translateY(-50%);
    width: 190px; height: 190px; background: var(--forest);
  }
  /* Back */
  .card-back { display: flex; align-items: center; justify-content: center; }
  .wordmark { display: flex; align-items: center; gap: 20px; }
  .wordmark-square { width: 62px; height: 62px; background: var(--forest); flex: none; }
  .wordmark-name {
    color: var(--white); font-weight: 600; font-size: 50px; line-height: 1; letter-spacing: .5px;
  }
  .wordmark-sub {
    color: var(--white); font-weight: 600; font-size: 20px; margin-top: 6px; letter-spacing: .5px;
  }
</style>
</head>
<body>
<main class="sheet">
  <section class="card card-front">
    <div class="person">
      <p class="person-name">Daniel Reeves</p>
      <p class="person-title">Managing Director</p>
    </div>
    <ul class="contact-list">
      <li class="contact-item">
        <svg viewBox="0 0 16 16" aria-hidden="true"><path d="M4 1.5c.8-.3 1.4 0 1.7.7l1 2.3c.2.6 0 1.1-.5 1.4l-1 .6c.6 1.6 1.7 2.8 3.3 3.5l.6-1c.3-.5.9-.7 1.4-.5l2.3 1c.7.3 1 .9.7 1.7-.6 1.8-2 2.6-3.9 2-3.6-1.2-6-3.7-7.2-7.3C1.8 3.9 2.4 2.2 4 1.5z" fill="var(--lime)"/></svg>
        555-310-4821
      </li>
      <li class="contact-item">
        <svg viewBox="0 0 16 16" aria-hidden="true"><rect x="4" y="1" width="8" height="14" rx="1.5" fill="none" stroke="var(--lime)" stroke-width="1.6"/><circle cx="8" cy="12.3" r="1" fill="var(--lime)"/></svg>
        555-310-7736
      </li>
      <li class="contact-item">
        <svg viewBox="0 0 16 16" aria-hidden="true"><rect x="1" y="3" width="14" height="10" fill="var(--lime)"/><path d="M1 3l7 5.5L15 3M1 13l5-4.5M15 13l-5-4.5" fill="none" stroke="var(--card)" stroke-width="1.2"/></svg>
        daniel@mailsample.com
      </li>
    </ul>
    <div class="brand-block"></div>
  </section>

  <section class="card card-back">
    <div class="wordmark">
      <div class="wordmark-square"></div>
      <div>
        <p class="wordmark-name">Verdant Cover</p>
        <p class="wordmark-sub">Australia Pty Ltd</p>
      </div>
    </div>
  </section>
</main>
</body>
</html>
```